Colin Marsh Optometry "we are moving" - to be used as a business card size magnet

Our optometry business "Colin Marsh Optometry" is moving location at the end of 2017. We plan to have business card size magnets printed to hand to our current customers to remind them that we are moving at the end of this year. We would like a clean, simple design that uses our logo and colour branding (see uploaded business card) with our new address "42 Wattle Lane Kelsobrook" our phone number "6732 1804" and "same great people, same great service" and "just next to the Silver Crest Dentist".

```html
<!DOCTYPE html>
<html lang="en">
<head>
<meta charset="utf-8">
<title>Colin Marsh Optometry – Moving Magnet</title>
<link rel="stylesheet" href="https://fonts.googleapis.com/css2?family=Roboto:wght@300;400;500;700;900&display=swap">
<style>
  :root {
    --page-bg: #e9e7ea;
    --card-purple: #4d3456;
    --band-purple: #3d2446;
    --text-white: #ffffff;
    --text-soft: #e6dcea;
  }
  * { box-sizing: border-box; margin: 0; padding: 0; }
  html, body {
    width: 1200px; height: 1200px; overflow: hidden;
    background: var(--page-bg);
    font-family: "Roboto", Arial, sans-serif;
  }
  .canvas {
    width: 1200px; height: 1200px;
    display: flex; align-items: center; justify-content: center;
  }
  .magnet-card {
    position: relative;
    width: 1000px; height: 612px;
    background: var(--card-purple);
    color: var(--text-white);
    overflow: hidden;
    box-shadow: 0 10px 30px rgba(40, 20, 50, 0.25);
    display: flex; flex-direction: column;
  }
  .moving-band {
    height: 78px;
    flex: none;
    background: var(--band-purple);
    display: flex; align-items: center; justify-content: center;
    font-weight: 300;
    font-size: 38px;
    letter-spacing: 2px;
    text-transform: uppercase;
    color: var(--text-soft);
  }
  .card-body {
    flex: 1;
    padding: 56px 40px 50px;
    display: flex; flex-direction: column; align-items: center;
  }
  .brand {
    display: flex; align-items: center; gap: 22px;
    margin-bottom: 34px;
  }
  .brand-dot {
    width: 34px; height: 34px; border-radius: 50%;
    background: var(--text-white);
  }
  .brand-name {
    font-weight: 500;
    font-size: 62px;
    letter-spacing: -0.5px;
    line-height: 1;
    color: var(--text-white);
  }
  .address {
    font-weight: 300;
    font-size: 36px;
    letter-spacing: 0.5px;
    color: var(--text-soft);
    line-height: 1.1;
  }
  .address-note {
    font-weight: 300;
    font-size: 24px;
    color: var(--text-soft);
    margin-top: 4px;
  }
  .phone {
    font-weight: 700;
    font-size: 36px;
    letter-spacing: 9px;
    margin-top: 18px;
  }
  .slogan {
    margin-top: auto;
    text-align: center;
    font-weight: 900;
    font-size: 42px;
    letter-spacing: 1px;
    text-transform: uppercase;
    white-space: nowrap;
  }
</style>
</head>
<body>
  <main class="canvas">
    <section class="magnet-card">
      <header class="moving-band">Moving location at the end of 2017</header>
      <div class="card-body">
        <div class="brand">
          <span class="brand-dot"></span>
          <span class="brand-name">Colin Marsh Optometry</span>
        </div>
        <p class="address">42 Wattle Lane Kelsobrook</p>
        <p class="address-note">( next to the Silver Crest Dentist )</p>
        <p class="phone">6732 1804</p>
        <p class="slogan">Same great people, same great service</p>
      </div>
    </section>
  </main>
</body>
</html>
```